Brightwell Comfort Contractors - Ductless Mini-Split Ad Creative Brief 4 qp ad images

Our Offers (Must Be Clearly Visible in the Design)
100% Satisfaction Guarantee
"We guarantee to keep you cool, or your money back! If you're not happy after we’ve had a chance to fix it, we’ll refund you!"

5-Year Labor Warranty
"That’s right – a 5-year labor warranty! No maintenance agreement required, just clean your filters each month!"

Chill-Wave Season 2025
"LIMITED-TIME OFFER: Get $999 off any ductless mini-split installation!"

Transparent Pricing
"What you see is what you pay—NO hidden fees!"

Ad Design Guidelines
Primary Focus: Ductless Mini-Split A/C Systems ONLY
Color Scheme: Must incorporate Brightwell Comfort Contractors' main colors with a hint of yellow to catch attention.
Look at truck wrap to get a feel for the border of ad image creative
Branding Elements: Include Brightwell Comfort logo prominently.
Contact Details: Display phone number clearly.
Trust Builders: Feature Chatterly & Zorvex review elements to enhance credibility.
Visibility: The offers must be clear and readable but not overcrowded. Prioritize readability and clean design.
Final Notes
Ensure the design is high-converting and visually engaging while maintaining a professional, premium feel.
The ad creatives will be used for ductless mini-split A/C systems only—this must be clear in the design messaging.
Feel Free to use your expertise and experience to make this better
Thank you 555-317-2946

```html
<!DOCTYPE html>
<html lang="en">
<head>
<meta charset="utf-8">
<title>Brightwell Comfort Contractors – Ductless Mini-Split Offer</title>
<link href="https://fonts.googleapis.com/css2?family=Poppins:wght@300;400;500;600;700;800;900&display=swap" rel="stylesheet">
<style>
  :root {
    --red: #c4262e;
    --blue: #0b6fbf;
    --ink: #2b2b2b;
    --badge: #6b6b6b;
    --gold: #f4b41a;
    --white: #ffffff;
  }
  * { margin: 0; padding: 0; box-sizing: border-box; }
  html, body { width: 1200px; height: 1200px; overflow: hidden; background: var(--white); }
  body { font-family: "Poppins", sans-serif; color: var(--ink); position: relative; }

  .brand { position: absolute; left: 80px; top: 96px; display: flex; align-items: center; gap: 14px; }
  .brand-dot { width: 58px; height: 58px; border-radius: 50%; background: var(--red); }
  .brand-name { font-weight: 700; color: var(--blue); font-size: 27px; line-height: 1.08; letter-spacing: 0.5px; }

  .headline { position: absolute; left: 78px; top: 222px; }
  .headline .percent { font-weight: 800; font-size: 150px; line-height: 1; letter-spacing: -6px; color: var(--ink); }
  .headline .satisfaction { font-weight: 800; font-size: 68px; line-height: 0.9; color: var(--blue); letter-spacing: -1.5px; margin-top: -4px; }
  .headline .guarantee { font-weight: 800; font-size: 78px; line-height: 0.9; color: var(--red); letter-spacing: -1px; margin-top: 2px; }
  .accent-bar { position: absolute; left: 80px; top: 496px; width: 59px; height: 6px; background: var(--blue); border-radius: 3px; }
  .promise { position: absolute; left: 80px; top: 518px; font-weight: 700; font-size: 27px; line-height: 1.35; text-transform: uppercase; }

  .hero-ring { position: absolute; left: 645px; top: 99px; width: 486px; height: 486px; border-radius: 50%; border: 14px solid var(--blue); }
  .hero-photo { position: absolute; left: 684px; top: 138px; width: 408px; height: 408px; border-radius: 50%;
    background: linear-gradient(160deg, #9a9a92 0%, #6e7a86 45%, #3f5066 100%); }

  .offer { position: absolute; top: 758px; width: 328px; height: 306px; border-radius: 20px; color: var(--white); text-align: center; }
  .offer.red { background: var(--red); }
  .offer.blue { background: var(--blue); }
  .offer-photo { position: absolute; left: 30px; top: -74px; width: 226px; height: 148px; border: 3px solid var(--white); border-top: none; border-radius: 0 0 22px 22px; }
  .offer-badge { position: absolute; left: 213px; top: -120px; width: 130px; height: 130px; }
  .offer-badge svg { width: 130px; height: 130px; }
  .offer-badge span { position: absolute; inset: 0; display: flex; align-items: center; justify-content: center; font-weight: 500; font-size: 16px; line-height: 1.3; color: var(--white); text-align: center; }
  .offer-body { position: absolute; left: 0; right: 0; top: 96px; }

  .warranty .t1 { font-weight: 800; font-size: 23px; line-height: 1.1; }
  .warranty .t2 { font-weight: 800; font-size: 34px; line-height: 1.1; }
  .warranty .t3 { font-weight: 700; font-size: 19px; line-height: 1.3; margin-top: 8px; }
  .warranty .t4 { font-weight: 400; font-size: 16px; line-height: 1.3; }

  .season .t1 { font-weight: 800; font-size: 24px; line-height: 1.2; }
  .season .t2 { font-weight: 700; font-size: 17px; line-height: 1.3; }
  .season .price { display: flex; align-items: center; justify-content: center; margin-top: 4px; }
  .season .get { font-weight: 400; font-size: 17px; transform: rotate(-90deg); width: 20px; }
  .season .amount { font-weight: 800; font-size: 46px; line-height: 1.1; }
  .season .off { font-weight: 300; font-size: 42px; line-height: 1.1; margin-left: 4px; }
  .season .t3 { font-weight: 400; font-size: 17px; line-height: 1.2; }

  .pricing .t1 { font-weight: 800; font-size: 24px; line-height: 1.2; }
  .pricing .t2 { font-weight: 700; font-size: 19px; line-height: 1.3; }
  .pricing .t3 { font-weight: 800; font-size: 24px; line-height: 1.1; margin-top: 4px; }
  .pricing .t4 { font-weight: 900; font-size: 46px; line-height: 1; }

  .contact { position: absolute; left: 78px; top: 1092px; display: flex; align-items: center; height: 48px; }
  .contact .phone { display: flex; align-items: center; gap: 8px; font-weight: 700; font-size: 40px; color: var(--ink); letter-spacing: -0.5px; }
  .divider { width: 2px; height: 36px; background: #bbb; margin: 0 10px; }
  .contact .web { font-weight: 600; font-size: 27px; color: var(--ink); }
  .rating { display: flex; align-items: center; gap: 6px; margin-left: 10px; }
  .rating .dot { width: 32px; height: 32px; border-radius: 50%; }
  .rating .dot.blue { background: var(--blue); }
  .rating .dot.red { background: var(--red); }
  .rating .meta { line-height: 1.1; }
  .rating .name { font-weight: 600; font-size: 11px; color: var(--ink); }
  .rating .stars { color: var(--gold); font-size: 11px; letter-spacing: 1px; }
  .rating .score { font-weight: 600; font-size: 10px; color: var(--ink); }

  .base-band { position: absolute; left: 0; bottom: 0; width: 1200px; height: 13px; background: var(--blue); }
</style>
</head>
<body>
<svg width="0" height="0" style="position:absolute">
  <defs>
    <polygon id="seal" points="64,0 54.1,14.5 55.4,32 39.6,39.6 32,55.4 14.5,54.1 0,64 -14.5,54.1 -32,55.4 -39.6,39.6 -55.4,32 -54.1,14.5 -64,0 -54.1,-14.5 -55.4,-32 -39.6,-39.6 -32,-55.4 -14.5,-54.1 0,-64 14.5,-54.1 32,-55.4 39.6,-39.6 55.4,-32 54.1,-14.5"/>
  </defs>
</svg>

<div class="brand">
  <div class="brand-dot"></div>
  <div class="brand-name">Brightwell Comfort<br>Contractors</div>
</div>

<div class="headline">
  <div class="percent">100%</div>
  <div class="satisfaction">SATISFACTION</div>
  <div class="guarantee">GUARANTEE</div>
</div>
<div class="accent-bar"></div>
<p class="promise">We guarantee to keep you<br>cool, or your money back!</p>

<div class="hero-ring"></div>
<div class="hero-photo" role="img" aria-label="Photo of a smiling homeowner and a technician standing beside an outdoor A/C unit"></div>

<div class="offer red warranty" style="left:81px">
  <div class="offer-photo" role="img" aria-label="Photo of the installation crew beside two mini-split outdoor units in the snow" style="background:linear-gradient(160deg,#d9d9d6,#8c8f92 60%,#eef0f2)"></div>
  <div class="offer-badge"><svg viewBox="-70 -70 140 140"><use href="#seal" fill="var(--badge)" stroke="#fff" stroke-width="3"/></svg><span>Only For<br>Ductless<br>Mini-Split<br>A/C</span></div>
  <div class="offer-body">
    <div class="t1">5-YEAR LABOR</div>
    <div class="t2">WARRANTY</div>
    <div class="t3">That’s right – a 5-year<br>labor warranty!</div>
    <div class="t4">No maintenance<br>agreement required</div>
  </div>
</div>

<div class="offer blue season" style="left:439px">
  <div class="offer-photo" role="img" aria-label="Photo of a technician giving a thumbs up in front of a mini-split unit" style="background:linear-gradient(160deg,#c9cfd4,#5f7a95 55%,#7d9a5a)"></div>
  <div class="offer-badge"><svg viewBox="-70 -70 140 140"><use href="#seal" fill="var(--badge)" stroke="#fff" stroke-width="3"/></svg><span>Only For<br>Ductless<br>Mini-Split<br>A/C</span></div>
  <div class="offer-body" style="top:92px">
    <div class="t1">CHILL-WAVE<br>SEASON 2025</div>
    <div class="t2">LIMITED-TIME OFFER</div>
    <div class="price"><span class="get">Get</span><span class="amount">$999</span><span class="off">OFF</span></div>
    <div class="t3">any ductless mini-split<br>installation!</div>
  </div>
</div>

<div class="offer red pricing" style="left:793px">
  <div class="offer-photo" role="img" aria-label="Photo of technicians servicing a mini-split unit against a stone wall" style="background:linear-gradient(160deg,#7a6a58,#a89478 50%,#3d4a5c)"></div>
  <div class="offer-badge"><svg viewBox="-70 -70 140 140"><use href="#seal" fill="var(--badge)" stroke="#fff" stroke-width="3"/></svg><span>Only For<br>Ductless<br>Mini-Split<br>A/C</span></div>
  <div class="offer-body" style="top:92px">
    <div class="t1">TRANSPARENT<br>PRICING</div>
    <div class="t2">What you see is what<br>you pay</div>
    <div class="t3">NO HIDDEN</div>
    <div class="t4">FEES!</div>
  </div>
</div>

<div class="contact">
  <div class="phone">
    <svg width="36" height="36" viewBox="0 0 24 24" aria-hidden="true"><path fill="var(--blue)" d="M6.6 10.8a15.1 15.1 0 0 0 6.6 6.6l2.2-2.2a1 1 0 0 1 1-.25 11.4 11.4 0 0 0 3.6.57 1 1 0 0 1 1 1V20a1 1 0 0 1-1 1A17 17 0 0 1 3 4a1 1 0 0 1 1-1h3.5a1 1 0 0 1 1 1c0 1.25.2 2.45.57 3.57a1 1 0 0 1-.25 1z"/></svg>
    555-317-2946
  </div>
  <div class="divider"></div>
  <div class="web">www.brightwellcomfortco.com</div>
  <div class="divider"></div>
  <div class="rating">
    <div class="dot blue"></div>
    <div class="meta"><div class="name">Chatterly</div><div class="stars">★★★★★</div><div class="score">5.0 RATING</div></div>
  </div>
  <div class="rating" style="margin-left:14px">
    <div class="dot red"></div>
    <div class="meta"><div class="name">Zorvex</div><div class="stars">★★★★★</div><div class="score">5.0 RATING</div></div>
  </div>
</div>

<div class="base-band"></div>
</body>
</html>
```